Buttons, Banners & MPUs - 'Coastal Getaway Digest'

We are launching a new product - a bookazine on sale later this month!

General description below:

COASTAL GETAWAY DIGESTS 2015

Calling all lovers of French holidays! Where will you go in 2015?

Let us guide you to the very best holidays in France with our brand new guide, featuring 180 pages of high quality and inspiring editorial and imagery. Coastal Getaways Digests 2015 provides a comprehensive, ideas-packed guide to classic breaks, as well as niche and new holiday ideas across France.

Love to get out in the French fresh air? We have activities such as boating, cycling and golf covered. There’s plenty for culture vultures and city breakers, too, plus lots of great ideas for family breaks including theme parks, zoos and attractions.

We whet the appetite of foodies and wine lovers, provide a guide to markets and festivals and also get off the beaten track with guides to driving, railway holidays and visit some of France’s most beautiful villages. And if you want to get creative, there are loads of ideas for photography, art, ‘me time’ escapes and tempting snapshots of some of France’s most unusual accommodation.

Whatever you love about France, there’s a fabulous French holiday made for you!

Design brief - bright, fun, exciting, inspiring.. with a clear call-to-action

We require a variety of sizes including:
300 x 250, 250 x 250, 728 x 90, 468 x 60, 120 x 600, 120 x 240, 600 x 200
- please only create a couple to showcase your design

More information can be found on the products website but please be aware that this is still under construction so please do not base your design on this: http://www.coastalgetawaydigests.example/

Target Market(s)

Francophiles, holiday makers, 40+, families, couples,

Industry/Entity Type

Construction

Font styles to use
Serif
Sans Serif

Requirements
Must have
• Logo
• Call to action
Nice to have
• Suggested strap lines:
• - The ultimate guide to holidays in France
• - The biggest and best guide to France
• - 180 pages of Fabulous French Holiday Ideas
• - What's New in 2015
Should not have
• Price - we want to direct traffic to our website which will reflect their local currency

```html
<!DOCTYPE html>
<html lang="en">
<head>
<meta charset="utf-8">
<title>Coastal Getaway Digest – Banners</title>
<link rel="stylesheet" href="https://fonts.googleapis.com/css2?family=Oswald:wght@500;600&display=swap">
<style>
  :root{
    --stage:#1b1b1b;
    --navy:#1b2a8c;
    --blue-deep:#0b2a6e;
    --blue-mid:#1553a8;
    --blue-light:#2f86cf;
    --white:#ffffff;
    --gold-top:#ffe23a;
    --gold-bottom:#f7a21a;
    --orange-top:#ffa53a;
    --orange-bottom:#e0620c;
    --photo-sky:#8fb3a0;
    --photo-green:#7a9a58;
    --photo-water:#3a8aa3;
    --cover-top:#4a9fd0;
    --cover-bottom:#b6c6a4;
  }
  *{box-sizing:border-box;margin:0;padding:0}
  html,body{width:1200px;height:911px;overflow:hidden}
  body{background:var(--stage);position:relative;font-family:"Oswald",Arial Narrow,sans-serif}

  .banner{position:absolute;overflow:hidden;background:linear-gradient(160deg,var(--blue-light),var(--blue-mid) 45%,var(--blue-deep))}
  .skyscraper{width:192px;height:721px;top:91px}
  .skyscraper.cycling{left:120px}
  .skyscraper.kayak{left:371px}
  .mpu{width:384px;height:319px;left:649px}
  .mpu.sailing{top:110px}
  .mpu.kayak{top:478px}

  .brand{position:absolute;color:var(--navy);font-weight:600;text-align:center;line-height:1}
  .brand .name{display:block;font-size:27px;letter-spacing:-.3px}
  .brand .edition{display:block;font-size:10px;margin-top:2px;letter-spacing:.5px}

  .skyscraper .logo-bar{position:absolute;left:0;top:0;width:100%;height:72px;background:var(--white)}
  .skyscraper .logo-bar::after{content:"";position:absolute;left:0;bottom:-6px;width:100%;height:6px;background:linear-gradient(90deg,var(--blue-deep),var(--blue-light))}
  .skyscraper .brand{left:0;right:0;top:16px}
  .skyscraper .photo{position:absolute;left:0;top:78px;width:100%;height:250px;clip-path:polygon(0 0,100% 0,100% 72%,0 100%)}

  .photo.cycling{background:linear-gradient(180deg,var(--photo-sky),var(--photo-green) 45%,#c3412f 60%,var(--photo-water))}
  .photo.kayak{background:linear-gradient(180deg,#6d8a55,#9b9580 35%,var(--photo-water) 60%,#d4b23a)}
  .photo.sailing{background:linear-gradient(180deg,#95b48c,#b59a62 35%,var(--photo-water) 65%,#c9d4db)}

  .cover{position:absolute;background:linear-gradient(180deg,var(--cover-top),var(--cover-bottom));border:2px solid var(--white);box-shadow:0 3px 8px rgba(0,0,0,.45)}
  .skyscraper .cover{left:22px;top:269px;width:144px;height:168px}

  .headline{position:absolute;text-align:center;font-weight:500;line-height:1.05}
  .headline .lead{color:var(--white)}
  .headline .hero{font-weight:600;background:linear-gradient(180deg,var(--gold-top),var(--gold-bottom));-webkit-background-clip:text;background-clip:text;color:transparent}
  .headline .question{color:var(--white)}

  .skyscraper .headline{left:0;right:0;top:443px}
  .skyscraper .lead{font-size:27px}
  .skyscraper .hero{font-size:38px;margin-top:6px;line-height:1}
  .skyscraper .question{font-size:22px;margin-top:14px;line-height:1.1}

  .cta{position:absolute;display:flex;align-items:center;justify-content:center;gap:5px;border-radius:5px;background:linear-gradient(180deg,var(--orange-top),var(--orange-bottom));color:var(--white);font-weight:500;box-shadow:0 2px 4px rgba(0,0,0,.4)}
  .cta svg{flex:none}
  .skyscraper .cta{left:18px;width:160px;top:662px;height:44px;font-size:23px}

  .mpu .photo{position:absolute;left:0;top:0;width:200px;height:262px}
  .mpu .panel{position:absolute;left:156px;top:0;width:228px;height:262px;background:linear-gradient(160deg,var(--blue-light),var(--blue-mid) 50%,var(--blue-deep));border-radius:60px 0 0 0/262px 0 0 0}
  .mpu .footer-strip{position:absolute;left:0;top:262px;width:100%;height:57px;background:linear-gradient(180deg,#e9edf4,var(--white))}
  .mpu .cover{left:18px;top:148px;width:144px;height:168px}
  .mpu .brand{left:180px;width:190px;top:272px}
  .mpu .brand .name{font-size:27px}
  .mpu .headline{left:170px;width:224px;top:12px}
  .mpu .lead{font-size:22px}
  .mpu .hero{font-size:38px;line-height:1.05}
  .mpu .question{font-size:21px;margin-top:10px;line-height:1.15}
  .mpu .cta{left:210px;width:158px;top:205px;height:44px;font-size:23px}
</style>
</head>
<body>

<section class="banner skyscraper cycling" aria-label="Skyscraper banner, cycling">
  <div class="logo-bar"><div class="brand"><span class="name">Coastal Getaway</span><span class="edition">Digests 2015</span></div></div>
  <div class="photo cycling" role="img" aria-label="Photo of a woman cycling beside a lake with a château behind"></div>
  <div class="cover" role="img" aria-label="Front cover of the Coastal Getaway Digests 2015 bookazine"></div>
  <div class="headline">
    <div class="lead">THE ULTIMATE<br>GUIDE TO</div>
    <div class="hero">HOLIDAYS<br>IN FRANCE</div>
    <div class="question">WHERE WILL<br>YOU GO IN 2015?</div>
  </div>
  <a class="cta">LEARN MORE<svg width="18" height="18" viewBox="0 0 18 18"><circle cx="9" cy="9" r="8.5" fill="#fff"/><path d="M4 9h8M9 5l4 4-4 4" stroke="#e0620c" stroke-width="2.4" fill="none" stroke-linecap="round" stroke-linejoin="round"/></svg></a>
</section>

<section class="banner skyscraper kayak" aria-label="Skyscraper banner, kayaking">
  <div class="logo-bar"><div class="brand"><span class="name">Coastal Getaway</span><span class="edition">Digests 2015</span></div></div>
  <div class="photo kayak" role="img" aria-label="Photo of two people kayaking past rocky cliffs"></div>
  <div class="cover" role="img" aria-label="Front cover of the Coastal Getaway Digests 2015 bookazine"></div>
  <div class="headline">
    <div class="lead">THE ULTIMATE<br>GUIDE TO</div>
    <div class="hero">HOLIDAYS<br>IN FRANCE</div>
    <div class="question">WHERE WILL<br>YOU GO IN 2015?</div>
  </div>
  <a class="cta">LEARN MORE<svg width="18" height="18" viewBox="0 0 18 18"><circle cx="9" cy="9" r="8.5" fill="#fff"/><path d="M4 9h8M9 5l4 4-4 4" stroke="#e0620c" stroke-width="2.4" fill="none" stroke-linecap="round" stroke-linejoin="round"/></svg></a>
</section>

<section class="banner mpu sailing" aria-label="MPU banner, sailing">
  <div class="photo sailing" role="img" aria-label="Photo of a sailing boat moored by a grassy riverbank"></div>
  <div class="panel"></div>
  <div class="footer-strip"></div>
  <div class="cover" role="img" aria-label="Front cover of the Coastal Getaway Digests 2015 bookazine"></div>
  <div class="brand"><span class="name">Coastal Getaway</span><span class="edition">Digests 2015</span></div>
  <div class="headline">
    <div class="lead">THE ULTIMATE GUIDE TO</div>
    <div class="hero">HOLIDAYS<br>IN FRANCE</div>
    <div class="question">WHERE WILL<br>YOU GO IN 2015?</div>
  </div>
  <a class="cta">LEARN MORE<svg width="18" height="18" viewBox="0 0 18 18"><circle cx="9" cy="9" r="8.5" fill="#fff"/><path d="M4 9h8M9 5l4 4-4 4" stroke="#e0620c" stroke-width="2.4" fill="none" stroke-linecap="round" stroke-linejoin="round"/></svg></a>
</section>

<section class="banner mpu kayak" aria-label="MPU banner, kayaking">
  <div class="photo kayak" role="img" aria-label="Photo of kayakers paddling past rocky cliffs"></div>
  <div class="panel"></div>
  <div class="footer-strip"></div>
  <div class="cover" role="img" aria-label="Front cover of the Coastal Getaway Digests 2015 bookazine"></div>
  <div class="brand"><span class="name">Coastal Getaway</span><span class="edition">Digests 2015</span></div>
  <div class="headline">
    <div class="lead">THE ULTIMATE GUIDE TO</div>
    <div class="hero">HOLIDAYS<br>IN FRANCE</div>
    <div class="question">WHERE WILL<br>YOU GO IN 2015?</div>
  </div>
  <a class="cta">LEARN MORE<svg width="18" height="18" viewBox="0 0 18 18"><circle cx="9" cy="9" r="8.5" fill="#fff"/><path d="M4 9h8M9 5l4 4-4 4" stroke="#e0620c" stroke-width="2.4" fill="none" stroke-linecap="round" stroke-linejoin="round"/></svg></a>
</section>

</body>
</html>
```